依頼概要
■依頼目的 / 概要
電子書籍Lumora本を出版いたしますので、
表紙デザイン作成をお願いいたします。

■納品物
下記での納品をお願い致します。

JPEG形式 及び PSD形式
横1600ピクセル x 縦2560ピクセル

■本の内容

<本のタイトル>
ソラノワ-SKY RING-
老職人に学んだ
はじめての家庭づくりのガイドブック

<著者名>
浅井徹郎

■デザイン要望
・本のタイトル / 著者名の反映をお願いします

デザインイメージ

・基本的に青系の色合い

・シンプルな背景にタイトル等のコピーを記載

・ターゲットは子どもを持つご両親。

・お子様の子育てに関する細かいノウハウというよりも、
最も要となる考え方をお伝えしています。

・信頼感のあるデザインを希望します。

<表現したいイメージなど>
・信頼感

<表現したくないイメージ>
・安っぽい
・嘘くさい
・大衆的

<利用画像について>
画像素材を使用される場合には、
商用利用可の素材をお願いします。

■その他
デザインを考えるのに必要な情報が他にございましたら、
お答えしますので、遠慮なくご連絡ください。

*添付ファイルは、過去電子書籍の表紙デザインです。
*ジャンルが異なりますので、デザインテイストは今回とは、異なります。
*あくまでも、表紙に出てくる要素(タイトルや著者名など)の参考としてご利用ください。

意図をしっかりとご理解いただき、
目につく素晴らしいデザインに仕上げていただきました。
ありがとうございます。

この度は応募いただきありがとうございました。
近いうちにまた同じく、表紙のデザインをお願いする予定です。
またご参加くださいませ。

```html
<!DOCTYPE html>
<html lang="ja">
<head>
<meta charset="utf-8">
<title>ソラノワ -SKY RING- 表紙</title>
<link rel="stylesheet" href="https://fonts.googleapis.com/css2?family=Montserrat:wght@900&family=Noto+Sans+JP:wght@500;700;900&display=swap">
<style>
  :root {
    --navy-deep: #1e2945;
    --navy-band: #2b4675;
    --white: #ffffff;
    --illust-tone: #e8a37f;
    --illust-tone-2: #4aa7a0;
    --balloon-tone: #e9b52d;
    --balloon-tone-2: #e36a4f;
  }
  * { margin: 0; padding: 0; box-sizing: border-box; }
  html, body { width: 750px; height: 1200px; overflow: hidden; background: var(--navy-deep); }
  .cover {
    position: relative;
    width: 750px;
    height: 1200px;
    background: var(--navy-deep);
    color: var(--white);
    font-family: "Noto Sans JP", sans-serif;
    overflow: hidden;
  }
  .lower-band {
    position: absolute;
    left: 0; top: 595px;
    width: 750px; height: 605px;
    background: var(--navy-band);
  }
  .series-title {
    position: absolute;
    top: 45px; left: 0; width: 750px;
    text-align: center;
    font-family: "Montserrat", sans-serif;
    font-weight: 900;
    font-size: 100px;
    line-height: 135px;
    letter-spacing: 2px;
  }
  .series-kana {
    position: absolute;
    top: 284px; left: 0; width: 750px;
    text-align: center;
    font-weight: 700;
    font-size: 24px;
    line-height: 32px;
    letter-spacing: 2px;
  }
  .author {
    position: absolute;
    top: 360px; left: 84px;
    writing-mode: vertical-rl;
    font-weight: 900;
    font-size: 56px;
    line-height: 1;
    letter-spacing: 6px;
  }
  .author-roman {
    position: absolute;
    top: 362px; left: 46px;
    writing-mode: vertical-rl;
    font-weight: 700;
    font-size: 17px;
    line-height: 1;
    letter-spacing: 1px;
  }
  .family-illustration {
    position: absolute;
    left: 250px; top: 412px;
    width: 388px; height: 292px;
  }
  .balloons-illustration {
    position: absolute;
    left: 552px; top: 830px;
    width: 128px; height: 170px;
  }
  .book-title { font-weight: 900; }
  .book-title span {
    position: absolute;
    left: 40px;
    display: block;
    white-space: nowrap;
    line-height: 1;
  }
  .book-title .lead { top: 716px; font-size: 72px; }
  .book-title .sub { top: 800px; font-size: 62px; }
  .book-title .main { top: 885px; font-size: 82px; }
  .book-title .main-last { top: 1015px; font-size: 95px; }
</style>
</head>
<body>
<main class="cover">
  <div class="lower-band"></div>

  <h1 class="series-title">SKY<br>RING</h1>
  <p class="series-kana">ソラノワ</p>

  <p class="author">浅井徹郎</p>
  <p class="author-roman">ASAI TETSURO</p>

  <svg class="family-illustration" role="img" aria-label="親子三人が寄り添うフラットなイラスト" viewBox="0 0 388 292">
    <defs>
      <linearGradient id="familyTone" x1="0" y1="0" x2="1" y2="1">
        <stop offset="0" stop-color="var(--illust-tone)"/>
        <stop offset="1" stop-color="var(--illust-tone-2)"/>
      </linearGradient>
    </defs>
    <rect x="0" y="0" width="388" height="292" rx="40" fill="url(#familyTone)" opacity="0.6"/>
  </svg>

  <h2 class="book-title">
    <span class="lead">老職人に学んだ</span>
    <span class="sub">はじめての</span>
    <span class="main">家庭づくりの</span>
    <span class="main-last">ガイドブック</span>
  </h2>

  <svg class="balloons-illustration" role="img" aria-label="二つの風船のイラスト" viewBox="0 0 128 170">
    <defs>
      <linearGradient id="balloonTone" x1="0" y1="0" x2="1" y2="0">
        <stop offset="0" stop-color="var(--balloon-tone)"/>
        <stop offset="1" stop-color="var(--balloon-tone-2)"/>
      </linearGradient>
    </defs>
    <rect x="0" y="0" width="128" height="170" rx="40" fill="url(#balloonTone)" opacity="0.8"/>
  </svg>
</main>
</body>
</html>
```